Funny Christmas Card for Pest Control Company

We area family owned pest control company, and we send out a Christmas card every year, we are looking for something funny that involves Christmas and Bugs.

Some possible examples.

1st example (this is the one we want): Santa's sleigh is being pulled by his 6 reindeer. Santa saw a spider come out of his bag of gifts so he is hugging (hugging as in both arms and legs around the first reindeer cause he is scared, like he is riding the reindeer and might fall off) the first reindeer farthest away from the sleigh. The reindeer closes to the sleigh says "Santa it is just a spider". Santa Says "Yes, but he was on the naughty list!"

Other options:
Rudolph the reindeer being scared cause he sees a spider
Something funny with pest control and Santa or Elves

Target Market(s)

Our Current Pest Control Customers

Industry/Entity Type

Pest Control

Requirements
Must have
• Funny and Pest control related
Should not have
• Swearing or sexual innuendos

```html
<!DOCTYPE html>
<html lang="en">
<head>
<meta charset="utf-8">
<title>Happy Holidays Card</title>
<link href="https://fonts.googleapis.com/css2?family=Sacramento&family=Montserrat:wght@500&display=swap" rel="stylesheet">
<style>
  :root {
    --paper: #ece3e0;
    --blush: #ecbcac;
    --stone: #847a6a;
    --ink: #7d7364;
    --ant-brown: #8a5a2a;
    --ant-red: #c22a4a;
  }
  html, body {
    margin: 0;
    padding: 0;
    overflow: hidden;
    background: var(--paper);
  }
  .card {
    position: relative;
    width: 1200px;
    height: 857px;
    background: var(--paper);
    overflow: hidden;
  }
  .card__shapes {
    position: absolute;
    inset: 0;
  }
  .greeting {
    position: absolute;
    margin: 0;
    font-family: "Sacramento", cursive;
    font-weight: 400;
    color: var(--ink);
    line-height: 1;
  }
  .greeting--happy {
    left: 650px;
    top: 70px;
    font-size: 190px;
  }
  .greeting--holidays {
    left: 440px;
    top: 245px;
    font-size: 210px;
  }
  .thanks {
    position: absolute;
    right: 112px;
    top: 493px;
    margin: 0;
    font-family: "Montserrat", sans-serif;
    font-weight: 500;
    font-size: 24px;
    letter-spacing: 2.6px;
    line-height: 38px;
    text-align: right;
    text-transform: uppercase;
    color: var(--ink);
  }
  .ant-parade {
    position: absolute;
    left: 417px;
    top: 610px;
    width: 714px;
    height: 235px;
    border-radius: 120px 120px 30px 30px;
    background: linear-gradient(90deg, var(--ant-brown) 0%, #a0682a 65%, var(--ant-red) 100%);
    opacity: 0.85;
  }
</style>
</head>
<body>
  <main class="card">
    <svg class="card__shapes" width="1200" height="857" viewBox="0 0 1200 857" aria-hidden="false">
      <path class="blob blob--left" d="M0 90 Q80 70 165 82 L225 560 Q228 600 190 600 L0 600 Z" fill="var(--blush)"/>
      <circle class="blob blob--corner" cx="1190" cy="60" r="115" fill="var(--blush)"/>
      <path class="swoop" d="M515 0 Q560 30 700 30 Q1000 25 1200 45" fill="none" stroke="var(--stone)" stroke-width="6" stroke-linecap="round"/>
      <g role="img" aria-label="Stylised grey Christmas tree decorated with pink looping garlands">
        <polygon class="tree" points="238,512 440,857 80,857" fill="var(--stone)"/>
      </g>
      <path class="post" d="M1165 857 L1160 650 Q1162 630 1180 632 Q1196 636 1195 660 L1200 857 Z" fill="var(--stone)"/>
    </svg>

    <h1 class="greeting greeting--happy">Happy</h1>
    <h1 class="greeting greeting--holidays">Holidays!</h1>

    <p class="thanks">Thank you for another year<br>of working together.</p>

    <div class="ant-parade" role="img" aria-label="Cartoon illustration of four smiling ants marching in a row, three brown and one red"></div>
  </main>
</body>
</html>
```